Flyer Design Dental Office Grand Opening offer

Dental office.

Grand opening flyer. Offer Exam + cleaning + xrays.
special: free teeth whitening ($200 value)

Target Market(s)

Middle class people around Huntington Beach.

Industry/Entity Type

Dental Clinic

Colors
cfeae6
86cfc6
fac994
fee18a
e667a6

Requirements
Must have
• Do not change my existing logo
Nice to have
• Have some appealing picture/design to catch the eye, but not too flashy
Should not have
• No cartoon kind of design

```html
<!DOCTYPE html>
<html lang="en">
<head>
<meta charset="utf-8">
<title>Bright Coast Dental – Grand Opening</title>
<link rel="stylesheet" href="https://fonts.googleapis.com/css2?family=Lato:wght@300;400;700;900&display=swap">
<style>
  :root {
    --page: #ffffff;
    --aqua-light: #e6f7f8;
    --aqua: #8fd6dc;
    --teal: #2aaab8;
    --teal-deep: #1a93a3;
    --violet: #7a6cb8;
    --purple: #5b2a86;
    --orange: #e8731f;
    --white: #ffffff;
  }
  * { margin: 0; padding: 0; box-sizing: border-box; }
  html, body {
    width: 1200px; height: 1200px; overflow: hidden;
    background: var(--page);
    font-family: "Lato", sans-serif;
  }
  .flyer {
    position: absolute; left: 160px; top: 32px;
    width: 880px; height: 1136px; overflow: hidden;
    background:
      radial-gradient(ellipse 60% 30% at 0% 45%, rgba(122,108,184,.85), transparent 70%),
      radial-gradient(ellipse 55% 28% at 100% 48%, rgba(122,108,184,.8), transparent 70%),
      radial-gradient(ellipse 50% 40% at 50% 70%, var(--aqua-light), transparent 75%),
      linear-gradient(180deg, #bfe6ee 0%, var(--aqua) 45%, #7fd0d8 70%, var(--aqua-light) 100%);
  }
  .hero-photo {
    position: absolute; left: 0; top: 0; width: 880px; height: 470px;
    background:
      radial-gradient(ellipse 45% 55% at 42% 40%, rgba(236,196,182,.9), transparent 70%),
      radial-gradient(ellipse 35% 50% at 70% 40%, rgba(214,172,150,.85), transparent 70%),
      linear-gradient(180deg, rgba(225,240,246,.9), rgba(143,214,220,0));
  }
  .headline, .services, .special, .bonus, .coverage, .brand, .doctor, .contact {
    position: absolute; left: 0; width: 880px; text-align: center;
  }
  .headline {
    top: 422px; font-size: 112px; font-weight: 900; letter-spacing: -3px;
    color: var(--white); line-height: 1.2;
    text-shadow: 0 4px 14px rgba(60,60,120,.35);
  }
  .services {
    top: 584px; font-size: 54px; font-weight: 900; letter-spacing: -1px;
    color: var(--purple); line-height: 1.1;
  }
  .services .plus { color: var(--orange); }
  .special {
    top: 656px; font-size: 58px; font-weight: 900; letter-spacing: -1px;
    color: var(--white); line-height: 1.1;
  }
  .special span {
    padding: 0 26px;
    background: radial-gradient(ellipse at center, rgba(42,170,184,.8), rgba(42,170,184,0) 72%);
  }
  .bonus {
    top: 736px; font-size: 48px; font-weight: 900; letter-spacing: -1px;
    color: var(--teal-deep); line-height: 1.1;
  }
  .bonus .highlight {
    color: var(--white);
    background: linear-gradient(90deg, rgba(122,108,184,0), rgba(122,108,184,.7) 20%, rgba(122,108,184,.7) 80%, rgba(122,108,184,0));
  }
  .coverage {
    top: 838px; font-size: 27px; color: var(--purple); line-height: 1.3;
  }
  .coverage .plans { font-weight: 900; margin-right: 18px; }
  .coverage .program { font-weight: 700; margin-right: 12px; }
  .brand {
    top: 900px; display: flex; justify-content: center; align-items: center; gap: 14px;
  }
  .brand-mark { width: 30px; height: 30px; background: var(--teal); }
  .brand-name { font-size: 50px; font-weight: 900; color: var(--teal-deep); letter-spacing: -0.5px; }
  .doctor {
    top: 1010px; font-size: 21px; color: var(--teal-deep); font-weight: 700;
  }
  .doctor .title { font-weight: 300; }
  .contact {
    top: 1062px; font-size: 25px; font-weight: 300; color: var(--violet);
  }
  .contact .phone { font-weight: 900; color: var(--purple); margin-left: 8px; }
</style>
</head>
<body>
  <main class="flyer">
    <div class="hero-photo" role="img" aria-label="Photo of a smiling mature couple, cheek to cheek"></div>
    <h1 class="headline">Grand Opening</h1>
    <p class="services">Exam <span class="plus">+</span> Cleaning <span class="plus">+</span> Xrays</p>
    <p class="special"><span>Special Offer</span></p>
    <p class="bonus">FREE <span class="highlight">Teeth Whitening</span> ($200 value)</p>
    <p class="coverage"><span class="plans">PPO, HMO</span><span class="program">CareState</span>welcomed</p>
    <div class="brand">
      <span class="brand-mark"></span>
      <span class="brand-name">Bright Coast Dental</span>
    </div>
    <p class="doctor">Lena Marsh <span class="title">DDS</span></p>
    <p class="contact">1280 Harbor Lane | Seaview Bay | CA 90000 <span class="phone">T (555) 014 – 2280</span></p>
  </main>
</body>
</html>
```